Red Kettle Pictures BIz Card

This will be a biz card for our independent film company
RED KETTLE PICTURES

we have a logo and i need to figure out how to post it to you!

Here is the info we need on the card:

LOGO

dorinda pratchek (lower case!)
dP@RedKettlePix.example
512-684-2273

Red Kettle Pictures, LLC
www.RedKettlePix.example

stories that matter (tagline)

Target Market(s)

adults in the entertainment industry in USA.
need something creative feeling, a bit funky, not to overt.
something eye catchy that people will be inclined to keep.

ask me any questions you have!

Industry/Entity Type

It Company

Requirements
Must have
• good looking! clean and easy to get the contact info. not too busy.
Nice to have
• love the cards where the design is "continued" on the back side.

perhaps the tag and logo on the back side?!?

open to ideas!
Should not have
• nothing "cartoonish"

```html
<!DOCTYPE html>
<html lang="en">
<head>
<meta charset="utf-8">
<title>Red Kettle Pictures – Business Card</title>
<link rel="stylesheet" href="https://fonts.googleapis.com/css2?family=Arimo:wght@400&display=swap">
<style>
  :root {
    --paper: #ffffff;
    --ink: #111111;
    --brand-red: #ee2e2e;
    --card-edge: #6b6b6b;
  }
  html, body {
    margin: 0;
    padding: 0;
    width: 1200px;
    height: 861px;
    overflow: hidden;
    background: var(--paper);
  }
  body {
    position: relative;
    font-family: "Arimo", Arial, sans-serif;
  }
  .card {
    position: absolute;
    left: 243px;
    width: 718px;
    height: 357px;
    border: 1px solid var(--card-edge);
    box-sizing: border-box;
    overflow: hidden;
    background: var(--paper);
  }
  .card--front { top: 25px; }
  .card--back { top: 481px; }

  /* front: straight red contact panel and a slim edge bar */
  .contact-panel {
    position: absolute;
    left: 200px;
    top: 120px;
    right: 0;
    bottom: 0;
    background: var(--brand-red);
  }
  .edge-bar {
    position: absolute;
    left: 0;
    top: 120px;
    width: 14px;
    bottom: 0;
    background: var(--brand-red);
  }
  .brand-name {
    position: absolute;
    left: 32px;
    top: 32px;
    margin: 0;
    display: flex;
    align-items: center;
    gap: 12px;
    font-size: 44px;
    font-weight: 400;
    line-height: 1;
    color: var(--ink);
    letter-spacing: -0.5px;
  }
  .brand-square {
    width: 18px;
    height: 18px;
    background: var(--brand-red);
    flex: none;
  }
  .contact {
    position: absolute;
    left: 230px;
    top: 165px;
    margin: 0;
    color: var(--paper);
    font-size: 19px;
    line-height: 23.5px;
    font-style: normal;
  }
  .contact p { margin: 0; }
  .contact .company { margin-top: 23px; }

  /* back: tagline with a plain red footer band */
  .tagline {
    position: absolute;
    left: 0;
    right: 0;
    top: 155px;
    margin: 0;
    text-align: center;
    font-size: 31px;
    font-weight: 400;
    color: var(--ink);
  }
  .footer-band {
    position: absolute;
    left: 0;
    right: 0;
    bottom: 0;
    height: 44px;
    background: var(--brand-red);
  }
</style>
</head>
<body>
  <section class="card card--front" aria-label="Card front">
    <div class="edge-bar" aria-hidden="true"></div>
    <div class="contact-panel" aria-hidden="true"></div>
    <h1 class="brand-name"><span class="brand-square"></span>Red Kettle Pictures</h1>
    <address class="contact">
      <p>dorinda pratchek</p>
      <p>dP@RedKettlePix.example</p>
      <p>512-684-2273</p>
      <p class="company">Red Kettle Pictures, LLC</p>
      <p>www.RedKettlePix.example</p>
    </address>
  </section>

  <section class="card card--back" aria-label="Card back">
    <p class="tagline">stories that matter</p>
    <div class="footer-band" aria-hidden="true"></div>
  </section>
</body>
</html>
```